Podcast cover art (not a logo)

I’m launching an audio-only podcast for parents of neurodivergent children. The podcast is meant to feel like a calm, trusted professional voice — not a brand or a performance.

Style direction:
--Clean and minimal
--Calm and grounded
--Professional, not playful
--Nothing flashy, loud, or busy
--No cartoon imagery

Content on the cover:
--Podcast title: Under the Quiet Surface
--Subtitle or tagline: Guiding Neurodivergent Children with Research and Respect (or Understanding Neurodivergent Kids)
--No episode numbers, no dates

Design preferences:
--Text-forward design
--Neutral or soft colors (muted blues, grays, off-whites)
--High contrast for readability at small sizes
--Simple, timeless font

What I do NOT want:
--A logo or branding system
--Illustrations of children or families
--Bright colors or playful graphics
--Trendy fonts or visual effects

Technical requirements:
--Square image
--3000 × 3000 pixels
--RGB color mode
--JPEG or PNG
--File size under 500 KB

Deliverables:
--Final cover art file
--Optional: one or two alternate background color versions

```html
<!DOCTYPE html>
<html lang="en">
<head>
<meta charset="utf-8">
<title>Under the Quiet Surface — Podcast Cover</title>
<link rel="stylesheet" href="https://fonts.googleapis.com/css2?family=Cinzel:wght@400;500&display=swap">
<style>
  :root {
    --page-bg: #eef1f1;
    --cover-light: #d6e3e4;
    --cover-mid: #b4cfd2;
    --cover-deep: #8fb6bc;
    --title-teal: #176d7c;
    --subtitle-ink: #121a1c;
    --line-white: #f7fbfb;
    --art-tone: #c4d9dc;
  }
  * { margin: 0; padding: 0; box-sizing: border-box; }
  html, body {
    width: 1018px;
    height: 1200px;
    overflow: hidden;
    background: var(--page-bg);
  }
  .canvas {
    position: relative;
    width: 1018px;
    height: 1200px;
  }
  .cover {
    position: absolute;
    left: 65px;
    top: 156px;
    width: 888px;
    height: 888px;
    background:
      radial-gradient(ellipse at 78% 20%, var(--cover-deep) 0%, transparent 45%),
      radial-gradient(ellipse at 8% 90%, var(--cover-deep) 0%, transparent 40%),
      linear-gradient(160deg, var(--cover-mid) 0%, var(--cover-light) 55%, var(--cover-mid) 100%);
    box-shadow: 0 6px 18px rgba(0, 0, 0, 0.18);
    font-family: "Cinzel", "Times New Roman", serif;
    text-align: center;
  }
  .cover-art {
    position: absolute;
    left: 287px;
    top: 185px;
    width: 291px;
    height: 199px;
    border-radius: 48% 52% 46% 40% / 55% 50% 45% 40%;
    background: radial-gradient(ellipse at center, var(--line-white) 0%, var(--art-tone) 75%);
    opacity: 0.75;
  }
  .podcast-title {
    position: absolute;
    left: 0;
    right: 0;
    top: 426px;
    font-size: 52px;
    font-weight: 400;
    letter-spacing: 1px;
    color: var(--title-teal);
    line-height: 1;
    white-space: nowrap;
  }
  .podcast-tagline {
    position: absolute;
    left: 0;
    right: 0;
    top: 503px;
    font-size: 32px;
    font-weight: 400;
    line-height: 40px;
    letter-spacing: 1px;
    color: var(--subtitle-ink);
    white-space: nowrap;
  }
  .mic-icon {
    position: absolute;
    left: 784px;
    top: 743px;
    width: 60px;
    height: 101px;
    opacity: 0.7;
  }
</style>
</head>
<body>
  <main class="canvas">
    <section class="cover">
      <div class="cover-art" role="img" aria-label="Line drawing of a brain made of interlocking puzzle pieces"></div>
      <h1 class="podcast-title">Under the Quiet Surface</h1>
      <p class="podcast-tagline">Guiding Neurodivergent Children<br>with Research and Respect</p>
      <svg class="mic-icon" viewBox="0 0 66 116" aria-hidden="true" fill="none" stroke="var(--line-white)" stroke-width="4" stroke-linecap="round">
        <rect x="15" y="3" width="36" height="70" rx="18"/>
        <line x1="20" y1="26" x2="30" y2="26"/>
        <line x1="20" y1="36" x2="30" y2="36"/>
        <line x1="20" y1="46" x2="30" y2="46"/>
        <line x1="36" y1="26" x2="46" y2="26"/>
        <line x1="36" y1="36" x2="46" y2="36"/>
        <line x1="36" y1="46" x2="46" y2="46"/>
        <path d="M5 48 v8 a28 28 0 0 0 56 0 v-8"/>
        <line x1="33" y1="84" x2="33" y2="106"/>
        <line x1="22" y1="110" x2="44" y2="110"/>
      </svg>
    </section>
  </main>
</body>
</html>
```